Velmora Biz Card 2019

New business card for Velmora Property Inspections. We are a residential home inspection company in Arizona.

Target Market(s)

Real Estate

Font styles to use
Sans Serif

Requirements
Must have
• Glen Mirewick
• Home Inspector
• Velmora Property Inspections, LLC
• 480-555-0172
• glen@velmora-llc.example

```html
<!DOCTYPE html>
<html lang="en">
<head>
<meta charset="utf-8">
<title>Velmora Property Inspections – Business Card Options</title>
<link href="https://fonts.googleapis.com/css2?family=Gentium+Book+Plus:ital,wght@0,400;0,700;1,400&display=swap" rel="stylesheet">
<style>
  :root {
    --green: #4bb848;
    --grey: #6d6e70;
    --grey-light: #8a8b8d;
    --rule: #b5b6b8;
    --paper: #ffffff;
    --edge: #231f20;
  }
  * { box-sizing: border-box; margin: 0; padding: 0; }
  html, body { width: 1200px; height: 1000px; overflow: hidden; background: var(--paper); }
  body { position: relative; font-family: "Gentium Book Plus", "Palatino Linotype", serif; }

  .card {
    position: absolute;
    left: 250px;
    width: 700px;
    height: 400px;
    border: 1px solid var(--edge);
    background: var(--paper);
    overflow: hidden;
  }
  .card--green { top: 75px; }
  .card--grey { top: 524px; }

  .card__band {
    position: absolute;
    left: 0; right: 0; bottom: 0;
    height: 62px;
    display: flex; align-items: center; justify-content: center;
    color: #fff;
    font-style: italic;
    font-size: 34px;
    letter-spacing: 0.2px;
  }
  .card--green .card__band { background: var(--green); }
  .card--grey .card__band { background: var(--grey); }

  .card__divider {
    position: absolute;
    width: 1px;
    background: var(--rule);
  }

  .wordmark {
    position: absolute;
    display: flex; align-items: center; gap: 12px;
    color: var(--green);
    font-weight: 700;
    font-size: 40px;
  }
  .wordmark__square { width: 34px; height: 34px; background: var(--green); }

  .person__name { font-weight: 700; font-size: 26px; color: var(--grey); line-height: 1.2; }
  .person__role { font-style: italic; font-size: 22px; color: var(--grey); line-height: 1.3; }

  .company { font-weight: 700; font-size: 33px; line-height: 40px; }
  .company--green { color: var(--green); }
  .company__line--grey { color: var(--grey); }
  .company__line--green { color: var(--green); }

  .contact { font-style: italic; font-size: 19px; color: var(--grey-light); line-height: 25px; }
  .contact__label { font-weight: 700; }
  .card--green .contact__label { color: var(--grey); }
  .card--grey .contact__label { color: var(--green); }

  .block { position: absolute; }
</style>
</head>
<body>

<section class="card card--green">
  <div class="wordmark" style="left:42px; top:120px;"><span class="wordmark__square"></span>Velmora</div>
  <div class="block" style="left:55px; top:228px;">
    <p class="person__name">Glen Mirewick</p>
    <p class="person__role">Home Inspector</p>
  </div>
  <div class="card__divider" style="left:332px; top:143px; height:177px;"></div>
  <div class="block" style="left:371px; top:163px;">
    <p class="company company--green">Velmora Property<br>Inspections, LLC</p>
  </div>
  <div class="block contact" style="left:371px; top:266px;">
    <p><span class="contact__label">T:</span> 480-555-0172</p>
    <p>glen@velmora-llc.example</p>
  </div>
  <div class="card__band">www.velmora-llc.example</div>
</section>

<section class="card card--grey">
  <div class="wordmark" style="left:72px; top:120px;"><span class="wordmark__square"></span>Velmora</div>
  <div class="block" style="left:39px; top:220px;">
    <p class="company"><span class="company__line--grey">Velmora Property</span><br><span class="company__line--green">Inspections, LLC</span></p>
  </div>
  <div class="card__divider" style="left:368px; top:143px; height:176px;"></div>
  <div class="block" style="left:441px; top:162px;">
    <p class="person__name">Glen Mirewick</p>
    <p class="person__role">Home Inspector</p>
  </div>
  <div class="block contact" style="left:441px; top:254px;">
    <p><span class="contact__label">T:</span> 480-555-0172</p>
    <p>glen@velmora-llc.example</p>
  </div>
  <div class="card__band">www.velmora-llc.example</div>
</section>

</body>
</html>
```